TW FITNESS Solutions logo & business card design.

TW FITNESS Solutions is a new business about to open in Toowoomba, Queensland, Australia. The TW stand for Megan Thorpe (me) the owner & operator of the business. The business includes two different areas. The first part is Life coaching & personal development & business coaching & the second part is fitness training in a group fitness with bootcamps and boxing for fitness & I'm also Personal Training sessions. So the line of "mind, body, life fitness comes into play") because I'm a one stop shop for people who are wanting to change their lives with NLP, hypnosis; life coaching & fitness training either all at once in a program or they choose just the life coaching or just the fitness side. I'm qualified as a fitness instructor with a Certificate III & Certificate IV, Senior first aide & CPR. I am certified as a NLP Practitioner & personal development coach. I want to create a business that changes peoples lives both inside & out as I am particularly passionate about changing woman's lives & so I'm running an 8 week programs just for women but in saying that I also want male clients for both sides of the business so I don't want the design to look like I only work with woman.
I would like the TW FITNESS to be in all capital letter and to be larger & stand out more than the word solutions which I would like in all lower case letters & not as large or bold as the TW FITNESS. I'm looking for a logo that captures whole body fitness & health focusing on the mind & body to create a happy healthy fit life! I would like vibrant colours that when you look at it you feel excited, happy & a new beginning at creating the best version of you & the best life you can have.

Industry/Entity Type

Life Coaching

Contact Information for Business Card

Business Name - TW FITNESS Solutions
Business heading information - Mind, Body & Life Fitness
Fitness & Life Coach -Megan Thorpe
Contact number - 0412873051
Email - contact@meganthorpe-example.com
Website - meganthorpe-example.com

```html
<!DOCTYPE html>
<html lang="en">
<head>
<meta charset="UTF-8">
<title>TW FITNESS Solutions – Business Card</title>
<link rel="stylesheet" href="https://fonts.googleapis.com/css2?family=Felipa&display=swap">
<style>
  :root {
    --paper: #ffffff;
    --frame-red: #d7141b;
    --edge-cyan: #5fe4f0;
    --text-light: #ffffff;
    --accent-magenta: #e23ce8;
    --photo-dark: #2c302b;
    --photo-mid: #454840;
    --photo-warm: #8a5a44;
    --photo-skin: #c07a58;
    --photo-pink: #d8306a;
    --photo-blue: #3c4478;
  }
  html, body {
    margin: 0;
    padding: 0;
    width: 1200px;
    height: 741px;
    overflow: hidden;
    background: var(--paper);
  }
  .card {
    position: relative;
    width: 1200px;
    height: 741px;
    background: var(--paper);
    font-family: "Felipa", Georgia, serif;
    font-weight: 400;
    color: var(--text-light);
  }
  .card-frame {
    position: absolute;
    left: 17px;
    top: 17px;
    width: 1157px;
    height: 695px;
    border: 4px solid var(--frame-red);
  }
  .card-face {
    position: absolute;
    left: 45px;
    top: 41px;
    width: 1107px;
    height: 650px;
    border: 2px solid var(--edge-cyan);
    overflow: hidden;
  }
  .boxer-photo {
    position: absolute;
    inset: 0;
    background:
      radial-gradient(ellipse 30% 8% at 72% 3%, rgba(216,48,106,0.85) 0%, rgba(216,48,106,0) 100%),
      radial-gradient(ellipse 18% 12% at 88% 82%, rgba(60,68,120,0.9) 0%, rgba(60,68,120,0) 100%),
      radial-gradient(ellipse 28% 50% at 86% 48%, var(--photo-skin) 0%, rgba(192,122,88,0.5) 50%, rgba(192,122,88,0) 100%),
      linear-gradient(90deg, var(--photo-dark) 0%, var(--photo-mid) 50%, var(--photo-warm) 78%, var(--photo-mid) 100%);
  }
  .business-name {
    position: absolute;
    left: 36px;
    top: 92px;
    margin: 0;
    font-weight: 400;
    white-space: nowrap;
    line-height: 1;
  }
  .business-name .brand {
    font-size: 52px;
    letter-spacing: 1px;
  }
  .business-name .descriptor {
    font-size: 38px;
  }
  .tagline {
    position: absolute;
    left: 42px;
    top: 290px;
    margin: 0;
    font-size: 35px;
    line-height: 58px;
    white-space: nowrap;
  }
  .coach-name {
    color: var(--accent-magenta);
    font-size: 44px;
  }
  .contact {
    position: absolute;
    left: 42px;
    top: 420px;
    margin: 0;
    font-size: 32px;
    line-height: 47px;
    white-space: nowrap;
  }
</style>
</head>
<body>
  <div class="card">
    <div class="card-frame"></div>
    <div class="card-face">
      <div class="boxer-photo" role="img" aria-label="Photo of a woman throwing a punch in pink boxing gloves, with colourful motion streaks"></div>
      <h1 class="business-name"><span class="brand">TW FITNESS</span> <span class="descriptor">solutions business</span></h1>
      <p class="tagline">Mind, Body &amp; Life Fitness Fitness &amp;<br>Life Coach ~ <span class="coach-name">Megan Thorpe</span></p>
      <p class="contact">Tel. 0412873051<br>Email: contact@meganthorpe-example.com<br>Website: meganthorpe-example.com</p>
    </div>
  </div>
</body>
</html>
```